Whiskey label design and bottle design

We need a label design for our new whiskey company. We are going to use paper logo that can include any elements that the designer wants including shinny, glossy, etc. We need something eye catching that stands out. Our bottle has not been chosen so we are can use any type of bottle including a custom bottle. Something that looks expensive. High quality. Need to stand out. The Brand name for now is the Heart of Marrowdale

Target Market(s)

21 to 54 60% male, 40% female

Industry/Entity Type

Whiskey Spirits

Requirements
Must have
• Detailed packaging, A barcode for the SKU, Governement warning on the back, Area for a story on the back, size of bottle on the back, Cork Closure.
Nice to have
• Something with tradition, Quality, and it stands out from comeptors. High quality labels.

```html
<!DOCTYPE html>
<html lang="en">
<head>
<meta charset="utf-8">
<title>Heart of Marrowdale – Bourbon Label</title>
<link rel="stylesheet" href="https://fonts.googleapis.com/css2?family=Archivo+Black&family=IM+Fell+English+SC&family=Playfair+Display+SC:wght@700;900&family=Roboto+Slab:wght@600;700&display=swap">
<style>
  :root {
    --backdrop: #2b2e31;
    --paper: #f4f4f1;
    --ink: #151515;
    --copper: #d69566;
    --engrave: #c9c9c6;
    --gold: #b88a4a;
    --band: #1c1a17;
    --rule: #a9a9a6;
  }
  * { margin: 0; padding: 0; box-sizing: border-box; }
  html, body { width: 800px; height: 1200px; overflow: hidden; }
  body { background: var(--backdrop); position: relative; }

  .neck-band {
    position: absolute; left: 250px; top: 110px; width: 300px; height: 64px;
    background: linear-gradient(180deg, #8d6a3a, var(--gold) 20%, #e2c48f 50%, var(--gold) 80%, #6e5230);
    display: flex; align-items: center; justify-content: center;
  }
  .neck-band__inner {
    width: 100%; height: 38px; background: var(--band);
    display: flex; align-items: center; justify-content: center; gap: 8px; white-space: nowrap;
    color: #d9b57a; font-family: "Roboto Slab", serif; font-weight: 700; font-size: 22px; letter-spacing: 1px;
  }
  .neck-band__inner em { font-family: "IM Fell English SC", serif; font-style: italic; font-size: 18px; font-weight: 400; text-transform: lowercase; }

  .label {
    position: absolute; left: 80px; top: 220px; width: 640px; height: 900px;
    background: var(--paper); overflow: hidden;
    box-shadow: 0 10px 30px rgba(0,0,0,.35);
  }
  .label__engraving {
    position: absolute; left: 40px; top: 24px; width: 560px; height: 600px;
    background:
      radial-gradient(ellipse at 50% 30%, rgba(201,201,198,.55), rgba(201,201,198,.15) 55%, transparent 75%),
      linear-gradient(180deg, rgba(201,201,198,.35), rgba(201,201,198,.1));
    border-radius: 40px 40px 8px 8px;
  }
  .label__arch { position: absolute; left: 0; top: 30px; width: 640px; height: 110px; }
  .label__arch text {
    font-family: "Playfair Display SC", serif; font-weight: 900; font-size: 26px;
    fill: var(--copper); letter-spacing: 1px;
  }
  .brand-title {
    position: absolute; left: 40px; top: 160px; width: 560px; text-align: center;
    font-family: "Playfair Display SC", serif; font-weight: 900; color: var(--ink);
    line-height: 1; white-space: nowrap; text-shadow: 4px 3px 0 var(--copper);
  }
  .brand-title__line1 { display: block; font-size: 86px; }
  .brand-title__line2 { display: block; font-size: 70px; }

  .style-name { position: absolute; left: 0; top: 400px; width: 640px; text-align: center; white-space: nowrap; }
  .style-name__top, .style-name__bottom {
    display: block; font-family: "Playfair Display SC", serif; font-weight: 700;
    color: var(--copper); font-size: 24px; line-height: 1.1;
  }
  .style-name__main {
    display: block; font-family: "Archivo Black", sans-serif; color: var(--ink);
    font-size: 58px; letter-spacing: 3px; line-height: 1.1;
  }
  .attributes {
    position: absolute; left: 34px; right: 40px; top: 590px;
    display: flex; justify-content: space-between; align-items: baseline; white-space: nowrap;
    font-family: "IM Fell English SC", serif; color: #333;
  }
  .attributes__left { font-size: 30px; }
  .attributes__right { font-size: 34px; }

  .info-panel {
    position: absolute; left: 14px; right: 14px; top: 690px; height: 190px;
    border: 3px solid var(--rule);
    font-family: "Roboto Slab", serif; color: var(--ink); white-space: nowrap;
  }
  .info-panel__labels {
    position: absolute; left: 30px; right: 150px; top: 14px;
    display: flex; justify-content: space-between; font-size: 16px; font-weight: 700; line-height: 20px;
  }
  .info-panel__wave-top { position: absolute; left: 70px; right: 30px; top: 44px; height: 14px; }
  .info-panel__specs {
    position: absolute; left: 80px; right: 30px; top: 64px; height: 40px;
    display: flex; align-items: center; gap: 22px;
    font-weight: 700; font-size: 28px; line-height: 40px;
  }
  .info-panel__divider { width: 2px; height: 32px; background: var(--rule); }
  .info-panel__owner { position: absolute; left: 80px; top: 110px; font-size: 15px; font-weight: 700; line-height: 20px; }
  .info-panel__wave { position: absolute; left: 70px; right: 30px; top: 138px; height: 36px; }
</style>
</head>
<body>
  <div class="neck-band">
    <div class="neck-band__inner">SPIRIT <em>of</em> QUALITY</div>
  </div>

  <main class="label">
    <div class="label__engraving" role="img" aria-label="Fine engraved ornamental frame pattern in pale grey"></div>

    <svg class="label__arch" viewBox="0 0 640 110">
      <path id="archPath" d="M150 100 Q320 20 490 100" fill="none"/>
      <text><textPath href="#archPath" startOffset="50%" text-anchor="middle">PRODUCT OF QUALITY</textPath></text>
    </svg>

    <h1 class="brand-title">
      <span class="brand-title__line1">Heart of</span>
      <span class="brand-title__line2">Marrowdale</span>
    </h1>

    <p class="style-name">
      <span class="style-name__top">Kentucky Straight</span>
      <span class="style-name__main">BOURBON</span>
      <span class="style-name__bottom">Whiskey</span>
    </p>

    <div class="attributes">
      <span class="attributes__left">Single Barrel</span>
      <span class="attributes__right">Cask Strength</span>
    </div>

    <section class="info-panel">
      <div class="info-panel__labels">
        <span>BOTTLE NO.</span>
        <span>BATCH NO.</span>
      </div>
      <svg class="info-panel__wave-top" viewBox="0 0 500 14" preserveAspectRatio="none">
        <path d="M0 7 Q12.5 0 25 7 T50 7 T75 7 T100 7 T125 7 T150 7 T175 7 T200 7 T225 7 T250 7 T275 7 T300 7 T325 7 T350 7 T375 7 T400 7 T425 7 T450 7 T475 7 T500 7" fill="none" stroke="var(--copper)" stroke-width="2"/>
      </svg>
      <div class="info-panel__specs">
        <span>90 PROOF</span><span class="info-panel__divider"></span>
        <span>750 ML</span><span class="info-panel__divider"></span>
        <span>45%VOL</span>
      </div>
      <p class="info-panel__owner">OWNER/DISTILLER:</p>
      <svg class="info-panel__wave" viewBox="0 0 500 36" preserveAspectRatio="none">
        <path d="M0 8 Q12.5 1 25 8 T50 8 T75 8 T100 8 T125 8 T150 8 T175 8 T200 8 T225 8 T250 8 T275 8 T300 8 T325 8 T350 8 T375 8 T400 8 T425 8 T450 8 T475 8 T500 8" fill="none" stroke="var(--copper)" stroke-width="2"/>
        <path d="M0 27 Q12.5 20 25 27 T50 27 T75 27 T100 27 T125 27 T150 27 T175 27 T200 27 T225 27 T250 27 T275 27 T300 27 T325 27 T350 27 T375 27 T400 27 T425 27 T450 27 T475 27 T500 27" fill="none" stroke="var(--copper)" stroke-width="2"/>
      </svg>
    </section>
  </main>
</body>
</html>
```